Book cover design for modern bagpipe music book

This music book will be A4 in size and requires a design for the front and back cover. The focus is on creating a modern and eye catching design, breaking away from the stereotypes of what people think of when they think of bagpipes. Think the OPPOSITE of a bagpiper in a full kilt standing on top of a mountain playing Copper Lanterns Rising!

Book title: Rise Hum March Rest

Other front cover text : Music for the bagpipes by Dermot Fairley

Front cover file ideas uploaded

2 pictures of bagpipes attached.

- The real set of bagpipes give an idea of the correct finer details

- The toy bagpipes perhaps have a better shape with the left 'stick' down

Back cover - No real brief. Keen for it not to be a full block single colour though.

Design requires 3mm bleed for print

Open to ideas and suggestions! Thank you!

```html
<!DOCTYPE html>
<html lang="en">
<head>
<meta charset="utf-8">
<title>Rise Hum March Rest — Music for the Bagpipes</title>
<link rel="stylesheet" href="https://fonts.googleapis.com/css2?family=Passion+One&family=Open+Sans:wght@300;700&display=swap">
<style>
  :root {
    --cover-bg: #000000;
    --ink: #ffffff;
    --placeholder: #d9d9d9;
  }
  html, body {
    margin: 0;
    padding: 0;
    width: 840px;
    height: 1200px;
    overflow: hidden;
    background: var(--cover-bg);
  }
  .cover {
    display: block;
    width: 840px;
    height: 1200px;
  }
  .icon-frame {
    fill: none;
    stroke: var(--ink);
    stroke-width: 8;
  }
  .icon-shape { fill: var(--ink); }
  .icon-line {
    fill: none;
    stroke: var(--ink);
    stroke-linecap: round;
  }
  .title-word {
    font-family: "Passion One", "Arial Black", sans-serif;
    font-size: 156px;
    fill: var(--ink);
  }
  .subtitle {
    font-family: "Open Sans", sans-serif;
    font-weight: 300;
    font-size: 34px;
    fill: var(--ink);
  }
  .author {
    font-family: "Open Sans", sans-serif;
    font-weight: 700;
    font-size: 47px;
    letter-spacing: 2px;
    fill: var(--ink);
  }
</style>
</head>
<body>
<svg class="cover" viewBox="0 0 840 1200" xmlns="http://www.w3.org/2000/svg">
  <!-- Icon column -->
  <g class="icon-column">
    <!-- Cutlery -->
    <rect class="icon-frame" x="98" y="188" width="156" height="156" rx="10"/>
    <g class="icon-cutlery">
      <line class="icon-line" x1="136" y1="226" x2="212" y2="305" stroke-width="10"/>
      <line class="icon-line" x1="214" y1="240" x2="140" y2="307" stroke-width="9"/>
      <path class="icon-shape" d="M204 226 l6 20 l14 -14 z"/>
      <line class="icon-line" x1="206" y1="224" x2="218" y2="236" stroke-width="3"/>
      <line class="icon-line" x1="212" y1="220" x2="222" y2="232" stroke-width="3"/>
    </g>

    <!-- Bed -->
    <rect class="icon-frame" x="98" y="372" width="156" height="156" rx="10"/>
    <g class="icon-bed">
      <rect class="icon-shape" x="120" y="412" width="9" height="73"/>
      <rect class="icon-shape" x="120" y="460" width="112" height="9"/>
      <rect class="icon-shape" x="224" y="460" width="9" height="25"/>
      <circle class="icon-shape" cx="141" cy="438" r="8"/>
      <path class="icon-shape" d="M152 432 h60 a14 14 0 0 1 14 14 v12 h-74 z"/>
    </g>

    <!-- Bagpipe pictogram area -->
    <rect class="icon-frame" x="98" y="556" width="156" height="156" rx="10"/>
    <rect x="128" y="584" width="96" height="100" rx="6" fill="var(--placeholder)"
          role="img" aria-label="White silhouette pictogram of a set of bagpipes"/>

    <!-- Repeat -->
    <rect class="icon-frame" x="98" y="738" width="156" height="156" rx="10"/>
    <g class="icon-repeat">
      <path class="icon-line" d="M146 848 A46 46 0 0 1 186 771" stroke-width="10"/>
      <path class="icon-shape" d="M182 758 l24 14 l-24 14 z"/>
      <path class="icon-line" d="M206 784 A46 46 0 0 1 166 861" stroke-width="10"/>
      <path class="icon-shape" d="M170 874 l-24 -14 l24 -14 z"/>
    </g>
  </g>

  <!-- Title -->
  <g class="title">
    <text class="title-word" x="308" y="318">RISE</text>
    <text class="title-word" x="308" y="502">HUM</text>
    <text class="title-word" x="308" y="686">MARCH</text>
    <text class="title-word" x="308" y="870">REST</text>
  </g>

  <text class="subtitle" x="417" y="1044" text-anchor="middle">MUSIC FOR THE BAGPIPES</text>
  <text class="author" x="420" y="1148" text-anchor="middle">BY DERMOT FAIRLEY</text>
</svg>
</body>
</html>
```